Business Card Design Project

Use newly designed logo and tie into newly designed website
I need a new logo and website layout designed for my partner's business. This is a birthday present. His business is interior painting, wallpapering and design. He also has access to a wide variety of products including carpet, fabrics, furniture, wallpaper, tile, countertops, etc. I have attached some screen shots of his website for reference. He is a one man shop and has a stellar reputation with his customers. He is on-time, very tidy, excellent with animals, and always finishes on time and on budget. There are no restrictions on colors or fonts. The logo needs to work well with the website, business cards and printed materials. The website needs to flow content for device size so it looks just as good on a cell phone or tablet as it does on a desktop computer. Whatever the heck that's called!Thanks. I am looking forward to seeing everyone's ideas.
Updates
Hi Designers,
We've reopened this project as our logo design project has just completed.
Please refer to the uploaded files and make use of either Horizontal or Vertical versions of the logo depending on what you think is suitable for your design proposals.
We look forward to your creative submissions!
Target Market(s)
Consumers looking to improve the interior environment of their homes by updating wall paint or paper, flooring (either carpet, tile, or hardwoods), counter tops, window treatments, etc. Clients tend to be more upper middle class and have certain taste levels and expectations. New logo, website and business card should align to meet those levels.
Industry/Entity Type
Cell Phone
Look and feel
Each slider illustrates characteristics of the customer's brand and the style your logo design should communicate.

```html
<!DOCTYPE html>
<html lang="en">
<head>
<meta charset="utf-8">
<title>Verandi Interior Designs – Business Card</title>
<link rel="stylesheet" href="https://fonts.googleapis.com/css2?family=Open+Sans:wght@400;600;700&display=swap">
<style>
  :root {
    --backdrop: #4a4a4a;
    --card: #f6f7f6;
    --brand: #85331f;
    --bar-light: #b06a2c;
    --ink: #111111;
    --rule: #c9c9c9;
  }
  html, body {
    margin: 0;
    width: 1200px;
    height: 999px;
    overflow: hidden;
    background: var(--backdrop);
    font-family: "Open Sans", Arial, sans-serif;
  }
  .card {
    position: absolute;
    left: 75px;
    top: 199px;
    width: 1050px;
    height: 600px;
    background: var(--card);
    overflow: hidden;
  }
  .brand {
    position: absolute;
    left: 70px;
    top: 290px;
    width: 420px;
    text-align: center;
    color: var(--brand);
    font-weight: 600;
    line-height: 1;
  }
  .brand-name {
    font-size: 62px;
    letter-spacing: 3px;
    display: block;
  }
  .brand-tagline {
    font-size: 30px;
    display: block;
    margin-top: 10px;
  }
  .divider {
    position: absolute;
    left: 589px;
    top: 225px;
    width: 1px;
    height: 151px;
    background: var(--rule);
  }
  .contacts {
    position: absolute;
    left: 620px;
    top: 236px;
    margin: 0;
    padding: 0;
    list-style: none;
  }
  .contact {
    display: flex;
    align-items: center;
    height: 47px;
    font-size: 22px;
    color: var(--ink);
  }
  .contact svg {
    width: 24px;
    height: 24px;
    margin-right: 16px;
    fill: var(--ink);
  }
  .person {
    position: absolute;
    left: 46px;
    top: 496px;
    color: var(--ink);
  }
  .person-name {
    font-size: 35px;
    font-weight: 700;
    margin: 0;
    line-height: 1.1;
  }
  .person-role {
    font-size: 27px;
    margin: 2px 0 0;
  }
  .bars {
    position: absolute;
    left: 0;
    top: 538px;
    width: 1050px;
    height: 62px;
  }
</style>
</head>
<body>
  <main class="card">
    <div class="brand">
      <span class="brand-name">VERANDI</span>
      <span class="brand-tagline">Interior Designs</span>
    </div>

    <div class="divider"></div>

    <ul class="contacts">
      <li class="contact">
        <svg viewBox="0 0 24 24" aria-hidden="true"><rect x="4" y="2" width="16" height="20" rx="3"/><rect x="7" y="5" width="10" height="13" fill="#f6f7f6"/></svg>
        (555) 214-3390
      </li>
      <li class="contact">
        <svg viewBox="0 0 24 24" aria-hidden="true"><path d="M2 10 L12 3 L22 10 V21 H2 Z"/><path d="M3 11 L12 17 L21 11" fill="none" stroke="#f6f7f6" stroke-width="1.5"/></svg>
        nate@verandidesigns.com
      </li>
      <li class="contact">
        <svg viewBox="0 0 24 24" aria-hidden="true"><circle cx="12" cy="12" r="10"/><g fill="none" stroke="#f6f7f6" stroke-width="1.4"><ellipse cx="12" cy="12" rx="4" ry="10"/><line x1="2" y1="12" x2="22" y2="12"/><line x1="12" y1="2" x2="12" y2="22"/><path d="M4 7 H20 M4 17 H20"/></g></svg>
        www.verandidesigns.com
      </li>
    </ul>

    <div class="person">
      <p class="person-name">Name Title</p>
      <p class="person-role">designation</p>
    </div>

    <svg class="bars" viewBox="0 0 1050 62" aria-hidden="true">
      <defs>
        <linearGradient id="barFade" x1="307" y1="0" x2="1050" y2="0" gradientUnits="userSpaceOnUse">
          <stop offset="0" stop-color="#b06a2c"/>
          <stop offset="1" stop-color="#85331f"/>
        </linearGradient>
      </defs>
      <g fill="url(#barFade)">
        <rect x="307" y="0" width="11" height="62"/>
        <rect x="330" y="0" width="24" height="62"/>
        <rect x="372" y="0" width="39" height="62"/>
        <rect x="420" y="0" width="54" height="62"/>
        <rect x="488" y="0" width="60" height="62"/>
        <rect x="561" y="0" width="75" height="62"/>
        <rect x="648" y="0" width="402" height="62"/>
      </g>
    </svg>
  </main>
</body>
</html>
```